Oil Field Service company needs professional business cards

Looking to clean up our current company business cards and look a little more professional. Harlow Tubular Services is a US based company that services the oil field. We deal with engineers, managers and oil rigs....................................................................................................................................................................................................................................................................................................................................................................................................

Target Market(s)

Oil and Gas professionals

Industry/Entity Type

Oil And Gas

Contact Information for Business Card

See attached photo as example

Font styles to use
Sans Serif

Colors
ec1f27

Requirements
Must have
• Company Logo, Name, Title, Cell, Office, Fax, Email.
• See attached photo
Nice to have
• External CRT, Internal CRT, Casing Crews, Torque Turn, Laydown Machine
Should not have
• Do not introduce any new pictures and keep it professional looking

```html
<!DOCTYPE html>
<html lang="en">
<head>
<meta charset="utf-8">
<title>Harlow Tubular Services – Business Card</title>
<link href="https://fonts.googleapis.com/css2?family=Source+Sans+3:wght@400;600;700&display=swap" rel="stylesheet">
<style>
  :root {
    --brand-red: #e31b23;
    --slate: #45525c;
    --ink: #3a3f44;
    --paper: #ffffff;
    --backdrop: #ecebe9;
  }
  * { margin: 0; padding: 0; box-sizing: border-box; }
  html, body {
    width: 1200px; height: 900px; overflow: hidden;
    background: var(--backdrop);
    font-family: "Source Sans 3", "Helvetica Neue", Arial, sans-serif;
  }
  .canvas { position: relative; width: 1200px; height: 900px; }
  .card {
    position: absolute;
    background: var(--paper);
    box-shadow: 0 4px 14px rgba(0,0,0,0.12);
    overflow: hidden;
  }
  .card-front { left: 238px; top: 62px; width: 555px; height: 342px; }
  .card-back  { left: 457px; top: 519px; width: 560px; height: 342px; }

  .band { position: absolute; left: 0; width: 100%; }
  .band-slate { background: var(--slate); height: 44px; }
  .band-red { background: var(--brand-red); height: 14px; }
  .band-top.band-slate { top: 0; }
  .band-top.band-red { top: 52px; }
  .band-bottom.band-red { bottom: 52px; }
  .band-bottom.band-slate { bottom: 0; }

  .identity {
    position: absolute; right: 308px; top: 122px;
    text-align: right;
  }
  .identity .person-name {
    color: var(--brand-red); font-weight: 600; font-size: 20px; line-height: 24px;
  }
  .identity .person-title {
    color: var(--ink); font-size: 16px; line-height: 20px;
  }

  .contact-list {
    position: absolute; left: 268px; top: 103px;
    list-style: none;
  }
  .contact-list li {
    display: flex; align-items: center;
    height: 20px;
    color: var(--ink); font-size: 16.5px;
  }
  .contact-list svg { width: 12px; height: 12px; margin-right: 9px; fill: var(--brand-red); flex: none; }

  .service-line {
    position: absolute; left: 0; right: 0; top: 223px;
    text-align: center; color: var(--ink); font-size: 16.5px; line-height: 22px;
  }

  .wordmark {
    position: absolute; left: 0; right: 0; top: 148px;
    text-align: center;
    color: var(--slate); font-weight: 700; font-size: 34px;
    letter-spacing: 1px;
  }
</style>
</head>
<body>
<main class="canvas">

  <section class="card card-front" aria-label="Card front">
    <div class="band band-top band-slate"></div>
    <div class="band band-top band-red"></div>

    <div class="identity">
      <div class="person-name">Wade Kellerman</div>
      <div class="person-title">Area Manager</div>
    </div>

    <ul class="contact-list">
      <li>
        <svg viewBox="0 0 24 24"><path d="M6.6 10.8a15.1 15.1 0 0 0 6.6 6.6l2.2-2.2c.3-.3.7-.4 1-.2 1.1.4 2.3.6 3.6.6.6 0 1 .4 1 1V20c0 .6-.4 1-1 1A17 17 0 0 1 3 4c0-.6.4-1 1-1h3.5c.6 0 1 .4 1 1 0 1.3.2 2.5.6 3.6.1.3 0 .7-.2 1z"/></svg>
        (405) 555-0142
      </li>
      <li>
        <svg viewBox="0 0 24 24"><path d="M7 1h10a2 2 0 0 1 2 2v18a2 2 0 0 1-2 2H7a2 2 0 0 1-2-2V3a2 2 0 0 1 2-2zm0 3v14h10V4zm5 15.5a1 1 0 1 0 0 2 1 1 0 0 0 0-2z"/></svg>
        (405) 555-0187
      </li>
      <li>
        <svg viewBox="0 0 24 24"><path d="M7 2h8l3 3v4h2a2 2 0 0 1 2 2v9a2 2 0 0 1-2 2H4a2 2 0 0 1-2-2v-9a2 2 0 0 1 2-2h3zm2 2v5h7V6h-2V4zm-2 9v2h2v-2zm4 0v2h2v-2zm4 0v2h2v-2zm-8 3v2h2v-2zm4 0v2h2v-2zm4 0v2h2v-2z"/></svg>
        (405) 555-0163
      </li>
      <li>
        <svg viewBox="0 0 24 24"><path d="M2 5h20v14H2zm2 2v.5l8 5 8-5V7l-8 5z"/></svg>
        wade.kellerman@harlowtubular.com
      </li>
    </ul>

    <p class="service-line">Laydown Machine | Casing Crew | Mud Tool | Torque Turn</p>

    <div class="band band-bottom band-red"></div>
    <div class="band band-bottom band-slate"></div>
  </section>

  <section class="card card-back" aria-label="Card back">
    <div class="wordmark">Harlow Tubular Services</div>
  </section>

</main>
</body>
</html>
```